Harbor Yield Group brochure

I need a standard 8 1/2 x 11 brochure and it must have a place for addresses and a stamp to mail located on the back (meet US postal requirements). I have logo and copy but will need a few unique images/icons to make it look great. I am a start up business development company that specializes in lead generation, blogging, social media, etc. Brochure must stand out in the mail and have that wow factor but must be clean as well. I would also like the topics provided to not stay within the lines of the folds on the brochure. Would like it to be free flowing without boundaries.

Please do no include the wine logo

Industry/Entity Type

Group

```html
<!DOCTYPE html>
<html lang="en">
<head>
<meta charset="utf-8">
<title>Harbor Yield Group – Brochure Inside Spread</title>
<link href="https://fonts.googleapis.com/css2?family=Cabin:ital,wght@0,400;0,500;0,600;1,400&family=Oswald:wght@400;500&display=swap" rel="stylesheet">
<style>
  :root{
    --backdrop:#e6e9eb;
    --paper:#ffffff;
    --teal:#2f6b80;
    --teal-dark:#245a6d;
    --sky:#45b4d9;
    --sky-light:#6cc6e3;
    --coral:#d8574c;
    --ink:#4c4c4c;
    --ink-soft:#8a8f93;
    --fold:#e3e6e8;
  }
  *{margin:0;padding:0;box-sizing:border-box}
  html,body{width:1200px;height:1000px;overflow:hidden;background:var(--backdrop)}
  body{font-family:"Cabin",sans-serif;color:var(--ink);position:relative}
  .spread{position:absolute;left:30px;top:60px;width:1140px;height:880px;background:var(--paper);box-shadow:0 2px 10px rgba(0,0,0,.12)}
  .fold{position:absolute;top:0;bottom:0;width:1px;background:var(--fold)}
  .abs{position:absolute}
  .title-main{font-size:18px;font-weight:500;color:var(--teal);line-height:1.1}
  .title-sub{font-size:16px;color:var(--ink);line-height:1.2}
  .tagline{font-style:italic;font-size:12px;color:var(--teal);line-height:1.5}
  .body-copy{font-size:12.5px;line-height:17.5px;color:var(--ink)}
  .column-copy{font-size:11.5px;line-height:17px;color:var(--ink-soft)}
  .caption{font-size:10px;line-height:14px;color:var(--ink-soft);text-align:center}
  .caption-small{font-size:8px;line-height:11px;color:var(--ink-soft);text-align:center}
  .stat-bar{position:absolute;bottom:285px;background:var(--teal);color:#fff;font-family:"Oswald",sans-serif;text-transform:uppercase;text-align:center;line-height:.95;padding-top:18px}
  .stat-bar .big{font-size:22px;display:block}
  .stat-bar .mid{font-size:17px;display:block}
  .stat-bar .small{font-size:8.5px;display:block;line-height:1.1}
  .stat-bar.tall{background:var(--sky);padding-top:8px}
  .stat-bar.highlight{background:var(--sky-light)}
  .stat-bar .accent{color:var(--coral)}
  .specialties{position:absolute;left:930px;top:10px;width:158px;height:165px;background:var(--sky);color:#fff;padding:10px 10px;font-size:9px;line-height:16.5px}
  .specialties em{display:block;opacity:.9}
  .art{position:absolute}
  .www{font-family:"Oswald",sans-serif;font-size:26px;letter-spacing:1px;color:var(--teal);font-weight:500}
  strong{font-weight:600}
</style>
</head>
<body>
<section class="spread">
  <div class="fold" style="left:370px"></div>
  <div class="fold" style="left:738px"></div>

  <!-- Panel: Strategic Brand Positioning -->
  <svg class="abs" style="left:22px;top:14px" width="80" height="80" viewBox="0 0 80 80"><path d="M40 6 A34 34 0 0 0 16 66" fill="none" stroke="var(--teal)" stroke-width="9"/></svg>
  <div class="abs" style="left:58px;top:42px">
    <div class="title-main">Strategic</div>
    <div class="title-sub">Brand Positioning</div>
  </div>
  <p class="abs tagline" style="left:20px;top:125px">It’s all about the Experience!</p>
  <p class="abs body-copy" style="left:20px;top:175px;width:330px">Great brands always start with a plan and nothing matters more to your business than your perceived value to potential customers. As you know, there are many other competitors in your niche. The process of becoming #1 can be extremely complicated because quite frankly every business niche is unique. Harbor Yield Group will position your business as the most recognized brand in your niche and THE ONLY LOGICAL CHOICE!</p>

  <svg class="abs" style="left:28px;top:345px" width="68" height="68" viewBox="0 0 68 68"><circle cx="34" cy="34" r="32" fill="var(--teal)"/><circle cx="34" cy="34" r="22" fill="#fff"/><path d="M34 34 L12 42 A22 22 0 0 0 56 42 Z" fill="var(--teal)"/></svg>
  <svg class="abs" style="left:142px;top:345px" width="68" height="68" viewBox="0 0 68 68"><circle cx="34" cy="34" r="32" fill="var(--teal)"/><circle cx="34" cy="34" r="22" fill="#fff"/><path d="M34 34 L34 12 A22 22 0 0 1 34 56 Z" fill="var(--teal)"/></svg>
  <svg class="abs" style="left:253px;top:345px" width="68" height="68" viewBox="0 0 68 68"><circle cx="34" cy="34" r="32" fill="var(--teal)"/><circle cx="34" cy="34" r="22" fill="#fff"/><path d="M34 34 L34 12 A22 22 0 1 1 17 48 Z" fill="var(--teal)"/></svg>

  <p class="abs column-copy" style="left:20px;top:455px;width:100px">Logos, color schemes and fonts play an important role in brand position but the most important piece in separating your brand from the rest is the experience potential customers associate your company with. This is the hardest part when creating a unique and recognizable brand.</p>
  <p class="abs column-copy" style="left:125px;top:455px;width:100px">Create a unique action plan that includes marketing, community involvement, increased website traffic, press releases and modifying your current public relations plan.</p>
  <p class="abs column-copy" style="left:235px;top:455px;width:100px">After you become the only logical choice in your niche, the last step is keeping your business #1. The creation of a master strategic plan will allow you to keep top of mind awareness for years to come.</p>

  <!-- Panel: Blogging -->
  <div class="abs" style="left:380px;top:48px;width:160px;text-align:right">
    <div class="title-main">Blogging</div>
    <div class="title-sub">to Generate Revenue</div>
  </div>
  <svg class="abs" style="left:528px;top:20px" width="56" height="90" viewBox="0 0 56 90"><path d="M18 8 A36 36 0 0 1 20 82" fill="none" stroke="var(--sky)" stroke-width="9"/></svg>
  <p class="abs tagline" style="left:395px;top:135px;width:165px">Not just for Nerds, Hipsters and Techies!</p>
  <p class="abs body-copy" style="left:395px;top:183px;width:182px;font-size:12px">Blogging has become so powerful if you are not blogging your company is falling in Searchly Search rankings (SEO). A recent study suggests businesses in the top 3 Searchly rankings generate 61.5% of the traffic. More website traffic paired with compelling online marketing content leads to more sales.</p>

  <div class="abs" style="left:380px;top:355px;width:1px;height:235px;background:#cfd4d7"></div>
  <div class="abs" style="left:380px;top:590px;width:345px;height:1px;background:#cfd4d7"></div>

  <div class="stat-bar" style="left:408px;width:47px;height:210px"><span class="big">77%</span><span class="big">OF</span><span class="small">Internet</span><span class="mid">Users</span><span class="mid">Read</span><span class="mid">Blogs</span></div>
  <div class="stat-bar" style="left:468px;width:47px;height:180px"><span class="big">57%</span><span class="big">OF</span><span class="small">Companies</span><span class="mid">With</span><span class="mid">A</span><span class="small">Blog have acquired a customer</span><span class="mid">From</span><span class="mid">Their</span><span class="small">Blog</span></div>
  <div class="stat-bar" style="left:527px;width:47px;height:185px"><span class="big">61%</span><span class="big">OF</span><span class="small">Consumers</span><span class="mid">Have</span><span class="small">Made Purchase</span><span class="mid">Based</span><span class="mid">On</span><span class="mid">Blog</span></div>
  <div class="stat-bar tall" style="left:588px;width:47px;height:595px"><span class="small">Websites</span><span class="mid">With</span><span class="mid">Blogs</span><span class="mid">Have</span><span class="mid">434%</span><span class="mid">More</span><span class="small">Indexed Pages</span></div>
  <div class="abs" style="left:646px;top:318px;font-family:'Oswald',sans-serif;color:var(--coral);line-height:1">
    <div style="font-size:12px">MOST</div><div style="font-size:7px">IMPORTANTLY!</div>
  </div>
  <div class="stat-bar highlight" style="left:649px;width:47px;height:245px"><span class="mid">Small</span><span class="small">Businesses</span><span class="mid">With</span><span class="mid">Blogs</span><span class="small">Generate</span><span class="mid accent">126%</span><span class="mid">More</span><span class="mid">Leads</span></div>

  <p class="abs column-copy" style="left:387px;top:620px;width:115px">We help you turn a blog into a MONEY making machine for your business:</p>
  <p class="abs column-copy" style="left:387px;top:705px;width:115px">We will teach you the correct way to blog and how to avoid some of the blogging blunders.</p>

  <svg class="abs" style="left:528px;top:622px" width="44" height="44" viewBox="0 0 44 44"><path d="M22 4 A18 18 0 1 1 6 14" fill="none" stroke="var(--coral)" stroke-width="1.8"/><path d="M4 10 L6 15 L11 13" fill="none" stroke="var(--coral)" stroke-width="1.8"/><path d="M22 10 V22 H31" fill="none" stroke="var(--coral)" stroke-width="1.8"/></svg>
  <p class="abs caption-small" style="left:500px;top:673px;width:100px">Spending too much time setting up a blog</p>
  <svg class="abs" style="left:635px;top:620px" width="56" height="42" viewBox="0 0 56 42"><g fill="var(--coral)"><circle cx="13" cy="10" r="6"/><rect x="5" y="17" width="16" height="18" rx="4"/><circle cx="43" cy="10" r="6"/><rect x="35" y="17" width="16" height="18" rx="4"/><circle cx="28" cy="15" r="7"/><rect x="18" y="23" width="20" height="19" rx="5"/></g></svg>
  <p class="abs caption-small" style="left:615px;top:673px;width:100px">Not knowing your audience</p>
  <svg class="abs" style="left:530px;top:725px" width="44" height="44" viewBox="0 0 44 44"><circle cx="22" cy="22" r="21" fill="var(--coral)"/><circle cx="22" cy="22" r="15" fill="none" stroke="#fff" stroke-opacity=".25" stroke-width="2"/></svg>
  <p class="abs caption-small" style="left:502px;top:780px;width:100px">No ‘call of action’</p>
  <div class="abs" style="left:640px;top:726px;width:42px;height:42px;background:var(--coral)"></div>
  <p class="abs caption-small" style="left:600px;top:780px;width:125px">Lack of compelling engaging content</p>

  <!-- Panel: Lead Generation -->
  <div class="abs" style="left:770px;top:35px;width:150px;text-align:center">
    <div class="title-main">Lead Generation</div>
    <div class="title-sub" style="font-size:15px">and conversion</div>
  </div>
  <svg class="abs" style="left:805px;top:76px" width="80" height="34" viewBox="0 0 80 34"><path d="M6 4 A36 28 0 0 0 74 4" fill="none" stroke="var(--sky)" stroke-width="8"/></svg>

  <div class="specialties">
    <em>Our other specialties:</em>
    Website Design &amp; Creation<br>
    Traditional Marketing Methods<br>
    Public Relations<br>
    SEO (Search Engine Optimization)<br>
    Event Management<br>
    Database/Email marketing<br>
    Social Media Management
  </div>

  <p class="abs tagline" style="left:763px;top:132px;width:160px">Just like speed dating… Well maybe not!</p>
  <p class="abs body-copy" style="left:763px;top:180px;width:165px">Ever wondered why a few businesses seem like they have so many leads they have to turn business away? It’s simple, they generate a massive amount of leads. Consumers don’t buy from every business they come into contact with so having tons of leads in your pipeline will make your business very profitable. You’re not a rocket scientist and neither are we, but we both know more leads translate into more sales!</p>

  <div class="art" role="img" aria-label="Illustration of social media icons rising from an open box" style="left:955px;top:200px;width:90px;height:95px;background:linear-gradient(160deg,var(--sky) 0%,var(--teal) 100%);border-radius:4px"></div>
  <p class="abs caption" style="left:925px;top:318px;width:150px">Using social media sites</p>

  <div class="abs www" style="left:790px;top:455px">WWW</div>
  <p class="abs caption" style="left:765px;top:518px;width:160px">Using your website and blog</p>

  <div class="art" role="img" aria-label="Illustration of a dollar sign card with a WOW burst" style="left:955px;top:400px;width:85px;height:90px;background:linear-gradient(160deg,var(--sky) 0%,var(--teal-dark) 100%);border-radius:4px"></div>
  <p class="abs caption" style="left:925px;top:515px;width:160px">Capturing more emails and creating special offers for potential customers</p>

  <div class="art" role="img" aria-label="Illustration of an envelope filled with direct mail pieces" style="left:795px;top:605px;width:80px;height:85px;background:linear-gradient(160deg,var(--sky) 0%,var(--teal-dark) 100%);border-radius:4px"></div>
  <p class="abs caption" style="left:760px;top:728px;width:160px">Using direct mail and other traditional marketing efforts which you are easily able to track results and see the impact of motivating offers.</p>

  <div class="art" role="img" aria-label="Illustration of an OFFERS banner with a WOW burst" style="left:945px;top:630px;width:120px;height:70px;background:linear-gradient(160deg,var(--sky-light) 0%,var(--teal) 100%);border-radius:4px"></div>
  <p class="abs caption" style="left:925px;top:728px;width:165px">Creating compelling email offers to your current database <strong style="color:var(--ink)">*businesses typically don’t understand how to make money from their current customers.</strong></p>
</section>
</body>
</html>
```